Web Page Template and Logo Design

We are launching a website to sell homewares and would like a logo design, as well as a home page template, and the template for the product pages.

The homewares store is called Brassy Walrus. The homewares we will sell will be edgy and very bright colours. We envisage the theme of the homepage will have hot pink, some blue/ white chinioserie pattern and potentially lime green. We would like the logo to reflect humour and "Brassy Walrus".

The images uploaded reflect the look and feel of the type of people who are our customers - they are not minimalists and they are definitely not into beige!

Target Market(s)

Predominantly women, 30 - 50

Industry/Entity Type

Store

Number of Pages Required

2 page

Font styles to use
Sans Serif

Colors
e34197
acd036
33a6d7

Requirements
Must have
• Template for home page and standard template for other pages;PLEASE NOTE: I have now listed the Brassy Walrus Logo as a separate 2 day listing; a bright, bold, colourful website with a sense of humour (it needs to dare people to put something bright in their homes).
• Please Note: I don't need a whole website, I have one of my staff who can do that for me. I just want the creative template for the homepage and a standard template for the product pages. It is the graphic design and creative side I am more interested in. I will want my staff member to be able to take the design and incorporate it into the website.

```html
<!DOCTYPE html>
<html lang="en">
<head>
<meta charset="utf-8">
<title>Brassy Walrus — Homewares</title>
<link rel="stylesheet" href="https://fonts.googleapis.com/css2?family=Oswald:wght@400;500&family=Open+Sans:wght@400;600&family=Lato:wght@700&display=swap">
<style>
:root{
  --pink:#e5186e;
  --pink-soft:#e8387f;
  --red:#e23a45;
  --ink:#222;
  --text:#444;
  --muted:#777;
  --rule:#e6e6e6;
  --panel:#f4f4f4;
  --bg-soft:#fafafa;
  --dark:#222;
  --star:#f0a417;
  --orange:#e88a1a;
  --lime:#a6d22c;
  --hot:#ec4a96;
  --cobalt:#2748a8;
  --porcelain:#eef1f8;
}
*{box-sizing:border-box;margin:0;padding:0}
html,body{width:1200px;height:2214px;overflow:hidden}
body{font-family:"Open Sans",Arial,sans-serif;color:var(--text);background:#fff;position:relative}
.wrap{position:absolute;left:173px;width:857px}

/* top bar */
.topbar{position:absolute;top:0;left:0;width:1200px;height:39px;background:var(--pink);color:#fff;font-size:13px}
.topbar .connect{position:absolute;left:173px;top:10px;font-weight:600}
.topbar .connect span{font-weight:400;margin-left:10px;font-size:12px}
.topbar .call{position:absolute;left:614px;top:10px;font-weight:600}
.topbar .call svg{vertical-align:-2px;margin:0 6px 0 14px}
.topbar .call span{font-weight:400}
.topbar .mail{position:absolute;left:858px;top:10px}
.topbar .mail svg{vertical-align:-1px;margin-right:8px}

/* header */
.header{position:absolute;top:39px;left:0;width:1200px;height:106px;background:#fff}
.logo{position:absolute;left:173px;top:30px;font-family:"Oswald",sans-serif;font-size:33px;font-weight:500;color:var(--pink);letter-spacing:.5px}
.nav{position:absolute;right:170px;top:43px;display:flex;gap:42px;font-size:15px;color:var(--ink)}

/* hero */
.hero{position:absolute;top:145px;left:0;width:1200px;height:568px;
  background:
    radial-gradient(ellipse 130px 150px at 900px 150px,rgba(70,150,40,.95),rgba(70,150,40,0) 100%),
    radial-gradient(ellipse 60px 70px at 910px 330px,rgba(190,120,30,.9),rgba(190,120,30,0)),
    radial-gradient(ellipse 60px 40px at 290px 310px,rgba(230,190,40,.9),rgba(230,190,40,0)),
    radial-gradient(ellipse 380px 170px at 400px 260px,rgba(242,232,212,.95),rgba(242,232,212,0)),
    radial-gradient(ellipse 60px 70px at 30px 80px,rgba(200,160,50,.9),rgba(200,160,50,0)),
    linear-gradient(180deg,#9a8c78 0%,#b9a78e 35%,#8e6a48 62%,#6b4526 78%,#3f2614 100%)}
.hero-copy{position:absolute;left:702px;top:228px;color:#fff;width:360px}
.hero-copy h1{font-family:"Oswald",sans-serif;font-weight:500;font-size:50px;line-height:1;letter-spacing:.5px}
.hero-copy p{font-size:18px;line-height:1.5;margin-top:18px}
.hero-arrow{position:absolute;top:279px;width:35px;height:35px;border-radius:50%;background:#2b2b2b;display:flex;align-items:center;justify-content:center}

/* features */
.features{position:absolute;top:713px;left:0;width:1200px;height:345px;background:var(--bg-soft);border-bottom:1px solid var(--rule)}
.feature{position:absolute;top:35px;width:267px;text-align:center}
.feature .photo{height:180px;border-bottom:3px solid var(--pink)}
.feature h3{font-size:17px;font-weight:400;color:var(--red);margin-top:13px;padding-bottom:12px;border-bottom:1px solid var(--rule)}
.feature p{font-size:11.5px;line-height:1.7;color:var(--muted);margin-top:13px}

/* gallery */
.gallery-head{top:1082px;height:40px}
.gallery-head h2{font-size:25px;font-weight:400;color:var(--red)}
.pager{position:absolute;right:0;top:8px;display:flex;gap:10px}
.pager span{width:18px;height:18px;border-radius:50%;border:1px solid #ddd;display:flex;align-items:center;justify-content:center}
.tile{position:absolute;width:273px;height:211px}
.tile-feature{background:
    radial-gradient(ellipse 120px 90px at 210px 40px,rgba(255,170,200,.45),rgba(255,170,200,0)),
    var(--pink-soft);color:#fff;text-align:center}
.tile-feature h3{font-family:"Lato",sans-serif;font-size:32px;margin-top:50px}
.tile-feature p{font-size:11.5px;margin-top:6px}
.tile-feature .link{width:38px;height:38px;border:2px solid #fff;border-radius:50%;margin:22px auto 0;display:flex;align-items:center;justify-content:center}

/* posts */
.post{position:absolute;top:1628px;width:260px}
.post .photo{height:142px}
.post h4{font-size:14px;font-weight:400;color:#555;margin-top:18px}
.post .meta{font-size:11.5px;color:#333;margin-top:13px}
.post .stars{color:var(--star);margin-left:16px;letter-spacing:1px}
.post p{font-size:11.5px;line-height:1.75;color:#555;margin-top:12px}
.testimonial{position:absolute;left:757px;top:1628px;width:272px;height:290px;background:var(--panel);padding:20px 20px}
.testimonial p{font-size:11.5px;line-height:1.77;color:#555;text-align:justify}
.testimonial .ago{font-size:11.5px;color:#333;margin-top:14px}
.author{display:flex;align-items:center;margin-top:26px;gap:14px;padding-left:4px}
.avatar{width:62px;height:62px;border-radius:50%;background:linear-gradient(160deg,#d9d2c8,#a99b8a);border:3px solid #fff}
.author b{display:block;font-size:11.5px;font-weight:600;color:var(--orange)}
.author span{font-size:11.5px;color:#555;line-height:2}
.testimonial .arrows{position:absolute;right:12px;bottom:6px;font-size:14px;color:#555;letter-spacing:6px}

/* clients */
.clients{position:absolute;left:173px;top:1975px;width:857px;height:92px;border:1px solid #eee;border-left:5px solid var(--pink);background:#fff}
.clients h2{position:absolute;left:28px;top:14px;font-size:28px;font-weight:400;line-height:1.1;color:var(--ink)}
.clients h2 em{font-style:normal;color:var(--pink);display:block}
.clients .divider{position:absolute;left:139px;top:12px;width:1px;height:66px;background:#eee}
.client-list{position:absolute;left:175px;top:32px;display:flex;gap:34px;font-size:20px;font-weight:600;color:#c9c9c9}
.client-list span{display:flex;align-items:center;gap:7px}
.client-list i{display:inline-block;width:22px;height:22px;border-radius:50%;background:#d6d6d6}

/* footer */
.footer{position:absolute;top:2108px;left:0;width:1200px;height:106px;background:var(--pink);color:#fff}
.footer .copy{position:absolute;left:173px;top:27px;font-size:11px}
.footer .links{position:absolute;left:173px;top:61px;font-size:11px}
.socials{position:absolute;left:551px;top:50px;display:flex;gap:8px}
.socials span{width:26px;height:26px;border-radius:50%;border:1px solid #fff;font-size:10px;font-weight:600;display:flex;align-items:center;justify-content:center}
.newsletter{position:absolute;left:756px;top:24px}
.newsletter h5{font-size:12px;font-weight:400;letter-spacing:.3px}
.newsletter form{display:flex;gap:12px;margin-top:12px}
.newsletter .field{width:185px;height:31px;background:var(--dark);color:#888;font-size:9px;padding:10px 14px}
.newsletter .btn{width:77px;height:31px;background:var(--dark);color:#fff;font-size:12px;display:flex;align-items:center;justify-content:center}
</style>
</head>
<body>

<div class="topbar">
  <div class="connect">Connect With Us :<span>Huddle · Chirrup · Feed · Linkwell</span></div>
  <div class="call">Call Us :<svg width="12" height="12" viewBox="0 0 12 12"><path d="M2 1h3l1 3-2 1c.6 1.4 1.6 2.4 3 3l1-2 3 1v3c-5 0-9-4-9-9z" fill="#fff"/></svg><span>+1 (555) 014-7733</span></div>
  <div class="mail"><svg width="13" height="9" viewBox="0 0 13 9"><rect width="13" height="9" fill="#fff"/><path d="M0 0l6.5 5L13 0" stroke="#e5186e" fill="none"/></svg>hello@brassywalrus.example</div>
</div>

<header class="header">
  <div class="logo">BRASSY WALRUS</div>
  <nav class="nav"><span>Home</span><span>About Us</span><span>Products</span><span>Gallery</span><span>Contact Us</span></nav>
</header>

<section class="hero" role="img" aria-label="Living room with cream sofa, coffee table with yellow and green mugs, potted topiary and wooden floor">
  <div class="hero-arrow" style="left:49px"><svg width="12" height="14" viewBox="0 0 12 14"><path d="M9 1L3 7l6 6" stroke="#fff" stroke-width="2.5" fill="none"/></svg></div>
  <div class="hero-copy">
    <h1>HOMEWARES</h1>
    <p>Nunc auctor elit sed dignissim mattis. Duis malesuada semper ipsum, non</p>
  </div>
  <div class="hero-arrow" style="left:1112px"><svg width="12" height="14" viewBox="0 0 12 14"><path d="M3 1l6 6-6 6" stroke="#fff" stroke-width="2.5" fill="none"/></svg></div>
</section>

<section class="features">
  <div class="feature" style="left:173px">
    <div class="photo" role="img" aria-label="Bright white lounge with sofa, framed pictures and a palm" style="background:radial-gradient(ellipse 40px 60px at 210px 80px,rgba(90,130,60,.6),rgba(90,130,60,0)),radial-gradient(ellipse 140px 40px at 120px 130px,#ffffff,rgba(255,255,255,0)),linear-gradient(180deg,#eeebe6,#d8d2c8 75%,#8d7a64)"></div>
    <h3>Homewares</h3>
    <p>Sed ut perspiciatis unde omnis iste natus error sit voluptatem accusantium doloremque</p>
  </div>
  <div class="feature" style="left:466px">
    <div class="photo" role="img" aria-label="Gilded console table with two grey upholstered chairs" style="background:radial-gradient(ellipse 110px 50px at 133px 80px,rgba(214,170,60,.95),rgba(214,170,60,0)),radial-gradient(ellipse 40px 50px at 50px 110px,rgba(150,150,160,.9),rgba(150,150,160,0)),radial-gradient(ellipse 40px 50px at 215px 110px,rgba(150,150,160,.9),rgba(150,150,160,0)),linear-gradient(180deg,#2c2c30,#3a3836 55%,#d8d4cc)"></div>
    <h3>Furniture</h3>
    <p>Sed ut perspiciatis unde omnis iste natus error sit voluptatem accusantium doloremque</p>
  </div>
  <div class="feature" style="left:762px">
    <div class="photo" role="img" aria-label="Red-walled art gallery with framed paintings and two visitors" style="background:radial-gradient(ellipse 60px 50px at 133px 80px,rgba(240,210,190,.8),rgba(240,210,190,0)),linear-gradient(180deg,#8a6a50 0%,#c0302e 25%,#b8262a 65%,#d8cfc4 85%,#bdb3a6)"></div>
    <h3>Art Work</h3>
    <p>Sed ut perspiciatis unde omnis iste natus error sit voluptatem accusantium doloremque</p>
  </div>
</section>

<section>
  <div class="wrap gallery-head" style="position:absolute">
    <h2>Gallery</h2>
    <div class="pager">
      <span><svg width="6" height="8" viewBox="0 0 6 8"><path d="M5 1L2 4l3 3" stroke="#777" fill="none"/></svg></span>
      <span><svg width="6" height="8" viewBox="0 0 6 8"><path d="M1 1l3 3-3 3" stroke="#777" fill="none"/></svg></span>
    </div>
  </div>
  <div class="tile" style="left:173px;top:1145px;background:radial-gradient(ellipse 60px 70px at 136px 130px,rgba(60,100,200,.85),rgba(60,100,200,0)),radial-gradient(ellipse 90px 100px at 136px 115px,rgba(25,30,25,.85),rgba(25,30,25,0)),radial-gradient(circle at 30px 40px,#c4ea3a,rgba(196,234,58,0) 60%),var(--lime)" role="img" aria-label="Black pagoda cabinet of blue and white china against lime chinoiserie wallpaper"></div>
  <div class="tile tile-feature" style="left:465px;top:1145px">
    <h3>Art Work</h3>
    <p>Lorem Ipsum is simply dummy</p>
    <div class="link"><svg width="18" height="18" viewBox="0 0 18 18" fill="none" stroke="#fff" stroke-width="2"><rect x="2" y="8" width="9" height="5" rx="2.5" transform="rotate(-45 6.5 10.5)"/><rect x="7" y="4" width="9" height="5" rx="2.5" transform="rotate(-45 11.5 6.5)"/></svg></div>
  </div>
  <div class="tile" style="left:756px;top:1145px;background:radial-gradient(ellipse 75px 90px at 136px 150px,var(--cobalt),rgba(39,72,168,0)),radial-gradient(ellipse 90px 40px at 136px 20px,rgba(90,160,60,.8),rgba(90,160,60,0)),radial-gradient(ellipse 60px 20px at 120px 10px,rgba(240,90,140,.9),rgba(240,90,140,0)),linear-gradient(135deg,#fbe3ee,#f08cb8 50%,#fbe3ee)" role="img" aria-label="Blue and white ginger jar with pink roses against pink trellis wallpaper"></div>
  <div class="tile" style="left:173px;top:1373px;background:radial-gradient(ellipse 80px 110px at 190px 100px,#f2e02a,rgba(242,224,42,0)),radial-gradient(ellipse 70px 90px at 40px 80px,rgba(245,240,240,.95),rgba(245,240,240,0)),radial-gradient(ellipse 60px 30px at 170px 200px,rgba(240,120,170,.9),rgba(240,120,170,0)),linear-gradient(135deg,#f6b8d2,#e8246e 60%,#c81a5a)" role="img" aria-label="Yellow wicker chair against bold pink and white floral wallpaper"></div>
  <div class="tile" style="left:465px;top:1373px;background:radial-gradient(ellipse 70px 60px at 230px 150px,rgba(230,40,80,.9),rgba(230,40,80,0)),radial-gradient(ellipse 60px 70px at 90px 120px,#ee4f93,rgba(238,79,147,0)),linear-gradient(180deg,#6a8fd0 0%,#f4f2f4 14%,#ffffff 30%,#f3d6e4 60%,#e06a8e 100%)" role="img" aria-label="White fireplace with pink trellis surround and floral armchair"></div>
  <div class="tile" style="left:756px;top:1373px;background:radial-gradient(ellipse 50px 70px at 130px 100px,rgba(240,244,250,.95),rgba(240,244,250,0)),radial-gradient(ellipse 30px 110px at 250px 110px,rgba(200,150,60,.95),rgba(200,150,60,0)),linear-gradient(180deg,#8c6a2c 0%,#3d5fb5 25%,#2a4aa8 55%,#c8d4ee 80%,#eef2fa)" role="img" aria-label="Blue and white porcelain jars on a blue patterned tablecloth beside a gilt column"></div>
</section>

<section>
  <article class="post" style="left:173px">
    <div class="photo" role="img" aria-label="Hallway with black and white tiled floor, stools and green chair" style="background:radial-gradient(ellipse 20px 40px at 150px 40px,rgba(40,170,90,.9),rgba(40,170,90,0)),linear-gradient(180deg,#ece9e4 0%,#d6d2cb 45%,#9a968f 60%,#e6e4e0 75%,#7d7a74)"></div>
    <h4>NULLAM LOREM MATTIS PURUS</h4>
    <div class="meta">29 Nov 2014<span class="stars">★★★☆☆</span></div>
    <p>Lorem ipsum dolor sit amet, consectetur piscing elit, sed do eiusmod tempor incididunt Lorem ipsum dolor sit amet, consectetur adipiscing elit, sed do eiusmod</p>
  </article>
  <article class="post" style="left:465px">
    <div class="photo" role="img" aria-label="Lime chinoiserie cabinet with blue and white china" style="background:radial-gradient(ellipse 80px 30px at 110px 25px,rgba(50,90,190,.9),rgba(50,90,190,0)),radial-gradient(ellipse 90px 70px at 100px 90px,rgba(25,30,25,.9),rgba(25,30,25,0)),var(--lime)"></div>
    <h4>NULLAM LOREM MATTIS PURUS</h4>
    <div class="meta">29 Nov 2014<span class="stars">★★★☆☆</span></div>
    <p>Lorem ipsum dolor sit amet, consectetur piscing elit, sed do eiusmod tempor incididunt Lorem ipsum dolor sit amet, consectetur adipiscing elit, sed do eiusmod</p>
  </article>
  <aside class="testimonial">
    <p>Duis dapibus aliquam mi, eget euismod scelerisque ut. Vivamus at elit quis urna adipiscing , Curabitur vitae velit in neque dictum blandit. Duis dapibus aliquam mi, eget euismod sceler ut.Duis dapibus aliquam mi, eget euismod scelerisque</p>
    <div class="ago">12 DAYS AGO</div>
    <div class="author">
      <div class="avatar" role="img" aria-label="Customer portrait"></div>
      <div><b>Marla</b><span>Duis dapibus aliquam</span></div>
    </div>
    <div class="arrows">‹ ›</div>
  </aside>
</section>

<section class="clients">
  <h2>Our<em>Client</em></h2>
  <div class="divider"></div>
  <div class="client-list">
    <span>Loomcraft</span>
    <span><i></i>Nebulon</span>
    <span>Kestrel</span>
    <span>Saffron Works</span>
    <span><i></i>Outlane</span>
  </div>
</section>

<footer class="footer">
  <div class="copy">©2014 Brassy Walrus , All Rights Reserved.</div>
  <div class="links">Home &nbsp;|&nbsp; About Us &nbsp;|&nbsp; Products &nbsp;|&nbsp; Gallery &nbsp;|&nbsp; Contact Us</div>
  <div class="socials" aria-label="Huddle, Chirrup, Reelbox"><span>H</span><span>C</span><span>R</span></div>
  <div class="newsletter">
    <h5>NEWSLETTER SIGN UP</h5>
    <form><div class="field">Enter Your Email</div><div class="btn">Subscribe</div></form>
  </div>
</footer>

</body>
</html>
```